Business Card Design Project

We need a business card design for a new company based in New York called "Quorra Mesh's". We do major installations of energy saving devices primarily LED lighting in large facilities. We would like a double sided card with our contact info on one side with our logo (to be designed) and on the other side the services we provide. We would like a heavy weight glossy card using the colors green and white. The final design should communicate environmental soundness and our market is very upscale corporations.
We would like our logo to illustrate LED lighting and we were thinking if we could get a stock picture of the Halvern Crest Building lit up on July 4th with red, white and blue LED lighting. The alternative would be anything that connotes environmentally proper thinking. It could be either a picture or a design.

```html
<!DOCTYPE html>
<html lang="en">
<head>
<meta charset="utf-8">
<title>Quorra Mesh's — Business Card</title>
<link rel="stylesheet" href="https://fonts.googleapis.com/css2?family=Tenor+Sans&family=Josefin+Sans:wght@400;600&display=swap">
<style>
  :root {
    --backdrop: #2a2a2a;
    --card: #f7f7f7;
    --card-shade: #e6e6e6;
    --ink-grey: #6b6b6b;
    --ink-dark: #4a4a4a;
    --leaf-green: #8cc21a;
  }
  * { margin: 0; padding: 0; box-sizing: border-box; }
  html, body {
    width: 1200px; height: 849px; overflow: hidden;
    background: var(--backdrop);
  }
  .canvas {
    position: relative; width: 1200px; height: 849px;
    display: flex; align-items: center; justify-content: center; gap: 60px;
  }
  .card {
    position: relative; width: 525px; height: 300px;
    background: linear-gradient(135deg, var(--card) 55%, var(--card-shade));
    box-shadow: 0 12px 30px rgba(0,0,0,.55);
  }
  .card-front {
    display: flex; align-items: center; justify-content: center;
  }
  .brand-name {
    font-family: "Tenor Sans", sans-serif;
    font-size: 50px; letter-spacing: 2px;
    color: var(--ink-grey);
  }
  .card-back .edge-band {
    position: absolute; left: 0; top: 0; bottom: 0; width: 12px;
    background: var(--leaf-green);
  }
  .contact-block {
    position: absolute; right: 34px; top: 46px; text-align: right;
    font-family: "Josefin Sans", sans-serif; text-transform: uppercase;
  }
  .person-name {
    font-size: 26px; font-weight: 400; letter-spacing: 1px;
    font-variant: small-caps; text-transform: none;
    color: var(--ink-dark);
  }
  .person-role {
    font-size: 10px; font-weight: 600; letter-spacing: 1.5px;
    color: var(--leaf-green); margin-top: 2px;
  }
  .contact-lines {
    margin-top: 58px;
    font-size: 13px; line-height: 19px; letter-spacing: 1px;
    color: var(--leaf-green);
  }
  .contact-lines .email { text-transform: lowercase; font-variant: small-caps; }
</style>
</head>
<body>
<main class="canvas">
  <section class="card card-front" aria-label="Card front">
    <h1 class="brand-name">Quorra Mesh's</h1>
  </section>
  <section class="card card-back" aria-label="Card back">
    <div class="edge-band"></div>
    <div class="contact-block">
      <p class="person-name">Dara Kellow</p>
      <p class="person-role">Sales Manager</p>
      <div class="contact-lines">
        <p>Address address address</p>
        <p>+1 212 555 0147</p>
        <p class="email">office@quorramesh.com &nbsp; quorramesh.com</p>
      </div>
    </div>
  </section>
</main>
</body>
</html>
```